Deliver a professional and engaging investment propsal.

I am appealing to highend smart investors and need a high quality, engaging and formal presentation in PDF.
DropBox: https://www.filemarsh.net/sh/q8wz3kdmv2tanp7/BCxRp4LfWmZq9TnYeJ2sKo7vH?dl=0
Text for project is in Dropbox called New Proposal Final
Along with past much older attempts of this job.
Any additional ideas to enable a better outcome would be appreicated.

```html
<!DOCTYPE html>
<html lang="en">
<head>
<meta charset="utf-8">
<title>Prairie Ridge Business Park – Project Proposal</title>
<link href="https://fonts.googleapis.com/css2?family=Roboto:wght@400;500;700&family=Open+Sans:ital,wght@0,400;0,600;0,700;1,600&display=swap" rel="stylesheet">
<style>
:root{
  --sky:#8ccbf5;
  --blue:#1c6fc4;
  --blue-deep:#0f4f9a;
  --navy:#163a6b;
  --ink:#2b2b2b;
  --grey:#4a4f57;
  --panel:#5b9bd2;
  --row:#dce9f7;
  --red:#d63b2f;
}
*{box-sizing:border-box;margin:0;padding:0}
html,body{width:1200px;height:1200px;overflow:hidden}
body{background:var(--sky);font-family:"Open Sans",Arial,sans-serif;color:var(--ink);position:relative}
.page{position:absolute;width:253px;height:358px;background:#fff;overflow:hidden}
.page.tall{height:362px}
.heading{font-family:"Roboto",Arial,sans-serif;font-weight:500;color:var(--blue);font-size:14.5px;display:flex;align-items:center;gap:4px;line-height:1}
.heading::before{content:"";width:10px;height:10px;border-radius:2px;background:var(--blue);flex:none}
.body{font-size:4.7px;line-height:1.4;color:var(--ink)}
.bullets{list-style:none}
.bullets li{position:relative;padding-left:6px;margin-bottom:5.2px}
.bullets li::before{content:"";position:absolute;left:0;top:1.5px;width:2.4px;height:2.4px;border-radius:50%;background:var(--blue)}
.footer{position:absolute;left:20px;right:14px;bottom:17px;border-top:.8px solid var(--blue)}
.footer span{position:absolute;left:50%;top:-1px;transform:translateX(-50%);background:var(--blue);color:#fff;font-size:4.3px;padding:1px 10px;font-family:"Roboto",Arial,sans-serif;white-space:nowrap;clip-path:polygon(6% 0,94% 0,100% 100%,0 100%)}
.ph{position:absolute}
/* cover */
.cover{background:linear-gradient(170deg,#8b939e 0%,#6c86a6 40%,#2d5f9a 100%)}
.cover .band{position:absolute;inset:0}
.cover-title{position:absolute;left:16px;top:18px;font-family:"Roboto",Arial,sans-serif}
.cover-title .kicker{font-weight:700;color:#2d333b;font-size:22px;line-height:.98;letter-spacing:.3px}
.cover-title .name{font-weight:500;color:var(--blue-deep);font-size:18px;margin-top:9px}
.cover-title .sub{font-weight:700;color:#1d2430;font-size:10px;line-height:1.2;margin-top:6px}
/* table */
.sens{width:100%;border-collapse:collapse;font-size:3.9px;font-family:"Open Sans",Arial,sans-serif}
.sens th{background:var(--blue);color:#fff;font-weight:600;padding:1.5px 2px;text-align:right}
.sens td{padding:1.6px 2px;text-align:right;border-bottom:.4px solid #fff}
.sens tr:nth-child(odd) td{background:var(--row)}
.sens .sec th{text-align:left;padding-left:40px}
.team-box{border-radius:6px;background:var(--blue);color:#fff;overflow:hidden;margin-bottom:9px}
.team-box h4{font-family:"Open Sans",Arial,sans-serif;font-style:italic;font-weight:600;font-size:6.5px;padding:4px 10px 2px;border-bottom:.6px solid rgba(255,255,255,.7)}
.team-box p{font-size:4.7px;line-height:1.4;padding:3px 10px 5px}
.contact-box{position:absolute;left:50px;right:48px;top:206px;border:.8px solid #fff;border-radius:4px;padding:10px 8px;color:#fff;font-family:"Roboto",Arial,sans-serif;text-align:center;background:rgba(120,130,140,.25)}
.contact-box h3{font-weight:400;font-size:8.2px;line-height:1.35;margin-bottom:6px}
.contact-line{display:flex;align-items:center;justify-content:center;gap:3px;font-size:7px;line-height:1.6}
.contact-line svg{width:7px;height:7px;flex:none}
.growth-box{background:var(--panel);border-radius:7px;padding:6px 12px 8px;margin:22px 16px 0;color:#10386a}
.growth-box h5{font-size:4.6px;font-weight:700;margin-bottom:3px}
.growth-box ol{font-size:4.5px;padding-left:50px;line-height:1.45}
.growth-box li{text-decoration:underline;color:#1e3f8a}
</style>
</head>
<body>

<!-- Row 1 : cover -->
<section class="page cover" style="left:328px;top:30px">
  <svg class="band" viewBox="0 0 253 358" width="253" height="358" aria-hidden="true">
    <polygon points="120,358 253,40 253,358" fill="#1c5ea8" opacity=".55"/>
    <polygon points="140,358 253,90 253,358" fill="#2a78c8" opacity=".5"/>
  </svg>
  <div class="ph" role="img" aria-label="Dusk photograph of a small-town main street with lit lamps and light trails" style="left:0;top:190px;width:253px;height:168px;background:linear-gradient(180deg,#3c6ca6 0%,#9a8f8a 45%,#4a4a58 100%);clip-path:polygon(0 100%,0 40%,120px 40%,253px 0,253px 100%)"></div>
  <div class="cover-title">
    <div class="kicker">PROJECT<br>PROPOSAL</div>
    <div class="name">Prairie Ridge Business Park</div>
    <div class="sub">60 ACRE MIXED-USE<br>DEVELOPMENT</div>
  </div>
</section>

<!-- Row 1 : intro page -->
<section class="page" style="left:619px;top:30px">
  <div class="ph" role="img" aria-label="Evening photograph of a three-storey extended stay hotel" style="left:0;top:0;width:253px;height:130px;background:linear-gradient(180deg,#2f5fa3 0%,#7d98b8 55%,#b39a84 80%,#8f8f8f 100%);clip-path:polygon(0 0,100% 0,100% 88%,0 100%)"></div>
  <div class="body" style="position:absolute;left:29px;right:25px;top:138px;color:var(--blue-deep)">
    <p style="margin-bottom:5px">We have an incredible property, Prairie Ridge Business Park, located at 1200 County Road 12, McKenzie County, Watford City, North Dakota, which we have fully funded with cash and now need a joint venture partner, buyer or lender to get this project to completion and producing a substantial profit we all can share.</p>
    <p style="margin-bottom:5px">Our property is located on the best oil reserves in the world in North Dakota USA, with more oil than any other county in the Bakken Basin and with the lowest recoverable costs of $24 a barrel.</p>
    <p>We own the property and need a partner to develop the site and bring to the market at half the cost of competing business parks in the area.</p>
  </div>
  <div class="ph" role="img" aria-label="Aerial site plan of the business park with lots, roads and green areas" style="left:29px;top:210px;width:198px;height:123px;background:linear-gradient(135deg,#9fb39a,#c9cfc6 50%,#8fa68b)"></div>
  <div class="footer"><span>Prairie Ridge Business Park</span></div>
</section>

<!-- Row 2 : participation -->
<section class="page" style="left:37px;top:416px">
  <h2 class="heading" style="position:absolute;left:16px;top:21px">Participation Options</h2>
  <ul class="bullets body" style="position:absolute;left:24px;right:16px;top:46px">
    <li>A joint venture partner would support all the costs developing the property without the upfront costs of the property purchase.</li>
    <li>All sales would be split to ensure both parties are paid out in such a way that both are paid out in full at the same time then a 50/50 profit share split on all remaining sales.</li>
    <li>Contract drawn up protecting and supporting both parties on agreed terms.</li>
    <li>As a potential joint venture partner, I would cover the full property (57.7 acres) cost as mentioned of $124,784 per acre (57.7 acres). ($7,200,000)</li>
    <li>Joint venture partner to supply the development costs estimated to be around $65,000 an acre estimated pending tender selection and additional refundable security bonds held with the city on development works.</li>
    <li>Development costs could be in up to three stages to lower outlay and limit exposure if so desired, however it will take longer to complete and bring to market.</li>
    <li>A buyer can be fully supported by myself to oversee the full project and outcomes and support the budgets of construction and sales to get the highest returns for a small fee.</li>
    <li>To purchase the property, you would need to contact me directly and I can introduce you to our realtor who will discount his commission from 6% to 5% which is a significant saving.</li>
    <li>Financing on excellent terms allowing 12 to 18 months for income streams and could be linked to a joint venture option / profit share.</li>
  </ul>
  <div class="footer"><span>Prairie Ridge Business Park</span></div>
</section>

<!-- Row 2 : site changes -->
<section class="page" style="left:328px;top:416px">
  <h2 class="heading" style="position:absolute;left:16px;top:21px">Major Site Changes</h2>
  <ul class="bullets body" style="position:absolute;left:24px;right:16px;top:44px">
    <li>We purchased the property in in 2013 for cash and without any additional debt, at the time we had highway frontage just outside city limits south of town with a zoning of agricultural within McKenzie County.</li>
    <li>2014 site zoning changed allowing a commercial zoning.</li>
    <li>Flag Hotel site purchased 2014 now with the option to purchase the franchise license and build the hotel ourselves.</li>
    <li>In 2016 we were added into City Limits which was a massive improvement to our site now taking advantage of confirmed city water and sewer was a great outcome.</li>
    <li>In 2016 the new bypass opened intersecting our highway frontage just 100 yards away which brings all the traffic in the Bakken right past our site which was a massive win for this project.</li>
    <li>Same commercial property listed across the road at $750,000 per acre retail at Bridgeton Commons and other business parks average listings $550,00 per acre.</li>
    <li>In late 2017 we applied for full site development application and were approved in mid-2018 which again was a significant improvement to the project.</li>
    <li>May 2018 full site infrastructure development approval which includes all roads and city services, this will trigger interest in the site from passing traffic and with a great marketing campaign will surely start sales coming in quickly once we break ground and start work.</li>
    <li>We also can buy the franchise license of the hotel for additional income potential if desired.</li>
  </ul>
  <div class="footer"><span>Prairie Ridge Business Park</span></div>
</section>

<!-- Row 2 : location -->
<section class="page" style="left:619px;top:416px">
  <h2 class="heading" style="position:absolute;left:16px;top:21px">Location</h2>
  <ul class="bullets body" style="position:absolute;left:24px;right:16px;top:43px">
    <li>Our property is ideally located in Watford City, United States of America, despite its humble beginnings, has suddenly found itself at the epicentre of the Bakken oil boom. Located in Western North Dakota the city has seen workers flood into the area over recent years to fill positions to support the growth.</li>
    <li>McKenzie County where Watford City is located has more recoverable oil and gas at the lowest recoverable cost per barrel at $24, making it most affordable anywhere in the Bakken basin, centrally located and very desirable area to establish a business and company headquarters.</li>
    <li>Watford City is the crossroads whereby around 20,000 vehicles pass by our site each day travelling locally and between towns. With established town and infrastructure, our project has highway frontage and is 100 yards away from the bypass intersection making it the best location in the county for this type of project.</li>
    <li>With billions invested into infrastructure in the past 5 years in and around the Bakken Shale Oil Basin our project has become the beneficiary of a major new bypass which intersects highway 85 just 100 yards south of our project, putting us on one of the busiest intersections in the Bakken. With this rapid growth we were included into the city limits providing additional benefits to the overall success for our development including all city services.</li>
    <li>Demand stems from the ongoing boom in oil and gas drilling in the area which is still in its infancy stages of life, North Dakota oil play and is expected to continue to grow well past 2050 based on obtainable reserves beneath the ground.</li>
  </ul>
  <div class="ph" role="img" aria-label="Regional county map of western North Dakota with oil counties highlighted in orange" style="left:0;top:230px;width:253px;height:93px;background:linear-gradient(90deg,#d9b542,#e2a63c 40%,#e7793a 55%,#d6b04a 100%)"></div>
  <div class="footer"><span>Prairie Ridge Business Park</span></div>
</section>

<!-- Row 2 : sensitivity -->
<section class="page" style="left:910px;top:416px">
  <h2 class="heading" style="position:absolute;left:16px;top:21px">Sensitivity Analysis</h2>
  <div class="body" style="position:absolute;left:16px;right:14px;top:42px;font-size:4.5px">
    <p style="font-weight:600">Sensitivity analysis is based on sales of the full site. (45 saleable acres) Our numbers below don't include revenue from build to suit projects or potential income stream from construction of the motel and various projects that could be developed on this 60-acre site.</p>
    <p style="color:var(--red);margin-top:3px">These costs are only shown as estimates at this stage.</p>
  </div>
  <table class="sens" style="position:absolute;left:21px;width:211px;top:75px">
    <tr><th>Estimated Projections</th><th>Projected</th><th>Best Scenario</th><th>Worst Scenario</th></tr>
    <tr><td>Average sale per acre (45)</td><td>$450,000</td><td>$500,000</td><td>$350,000</td></tr>
    <tr><td>Total Sales</td><td>$20,250,000</td><td>$22,500,000</td><td>$15,750,000</td></tr>
    <tr class="sec"><th colspan="4">Projected Expenses</th></tr>
    <tr><td>Engineers</td><td>$250,000</td><td>$190,000</td><td>$300,000</td></tr>
    <tr><td>Estimated Site Development Works</td><td>$2,400,000</td><td>$2,000,000</td><td>$3,500,000</td></tr>
    <tr><td>Site Licences / Permits</td><td>$450,000</td><td>$350,000</td><td>$500,000</td></tr>
    <tr><td>Additional Signage, Marketing</td><td>$20,000</td><td>$15,000</td><td>$25,000</td></tr>
    <tr><td>Professional Fees</td><td>$135,000</td><td>$130,000</td><td>$145,000</td></tr>
    <tr><td>Attorney Contracts / Support</td><td>$45,000</td><td>$30,000</td><td>$50,000</td></tr>
    <tr><td>Realtor Commissions</td><td>$1,000,000</td><td>$900,000</td><td>$1,200,000</td></tr>
    <tr><td>Property Payout</td><td>$7,200,000</td><td>$7,200,000</td><td>$7,200,000</td></tr>
    <tr><td>Estimated Projected Full Costs</td><td>$11,500,000</td><td>$10,815,000</td><td>$12,920,000</td></tr>
    <tr><td>Estimated Projected Per Acre Costs</td><td>$255,000</td><td>$240,000</td><td>$287,000</td></tr>
    <tr><td>Estimated Total Projected Profit</td><td>$8,750,000</td><td>$11,685,000</td><td>$2,830,000</td></tr>
    <tr><td>Estimated Profit Each Partner</td><td>$4,375,000</td><td>$5,842,500</td><td>$1,415,000</td></tr>
  </table>
  <p class="body" style="position:absolute;left:21px;right:18px;top:256px;font-style:italic;font-weight:700;font-size:4.6px">This investment may offer an opportunity for a visa into the USA however you will need to undertake your own inquiries.</p>
  <div class="footer"><span>Prairie Ridge Business Park</span></div>
</section>

<!-- Row 3 : growth + hotel -->
<section class="page tall" style="left:34px;top:798px">
  <div class="growth-box">
    <h5>ADDITIONAL LOCATION GROWTH:</h5>
    <ol>
      <li>Halvorsen Energy 150 million-dollar city investment 2018</li>
      <li>North Dakota is the nation's second-biggest oil producer</li>
      <li>McKenzie County Investment, Development</li>
      <li>Watford City's brighter future</li>
    </ol>
  </div>
  <div class="body" style="position:absolute;left:17px;right:15px;top:84px">
    <p style="margin-bottom:5px">Within the 100 yards of Prairie Ridge Business park, directly across the road commercial land is currently listed at of $750,000 an acre at Bridgeton Commons and many more locations up to $650,000 per acre. With an advantage over other sites in terms of a better location and much lower purchase and development costs the numbers don't lie, and we need to have pad ready to build lots to offer the market.</p>
    <p style="margin-bottom:5px">Bakken traffic, North, South, East and West will have to travel right by our site making it the second busiest intersection in the Bakken area, giving us the best exposure to sell, promote and grow, this site can and will be the location for new business and growth, we need to develop the site now to move forward.</p>
    <p>With our obvious high exposure to potential buyers through the passing traffic and lower entry price point there is no doubt Prairie Ridge Town Center will become the place where business will want to build alongside a quality business like the Northstar Suites Extended Stay Hotel.</p>
  </div>
  <h2 class="heading" style="position:absolute;left:17px;top:197px;font-size:14px;align-items:flex-start;line-height:1.02">Northstar Suites<br>Extended Stay</h2>
  <div class="body" style="position:absolute;left:17px;right:15px;top:230px">
    <p style="margin-bottom:5px">Northstar Hospitality Group's unmatched experience and leadership in the hotel industry designed a new extended stay hotel that satisfy one of the most in-demand needs of today's business and leisure travellers.</p>
    <p>Here guests will experience the very best in hotel and home. Its flexible spaces, stylish design, and brand signature elements come together to create an enriching extended stay experience for your guests, while building loyalty and repeat bookings for your hotel.</p>
  </div>
  <div class="footer"><span>Prairie Ridge Business Park</span></div>
</section>

<!-- Row 3 : team + conclusion -->
<section class="page tall" style="left:328px;top:798px">
  <h2 class="heading" style="position:absolute;left:18px;top:20px">About Our Quality Team</h2>
  <div style="position:absolute;left:18px;right:14px;top:43px">
    <div class="team-box">
      <h4>Owner - Daniel Harlow</h4>
      <p>I am an investor always seeking great value opportunities.</p>
    </div>
    <div class="team-box">
      <h4>Our KRM Engineering Design and Planning</h4>
      <p>From planning to conceptual design to construction services, our planning department understands the innovative solutions needed for your project needs. Our planners collaborate with other design professions to create innovative solutions for planning projects and other design needs. KRM designs with nature in mind and creating sustainable solutions to each unique and individual design requirement. Our pursuit is to bring the public a service with solid goals and concepts by challenging old convention and implementing new life-giving communities and spaces.<br><br>We have experience and capabilities in conceptual project development, master planning, feasibility studies, park and recreational design, urban and land planning.</p>
    </div>
  </div>
  <h2 class="heading" style="position:absolute;left:18px;top:189px">In Conclusion</h2>
  <div class="body" style="position:absolute;left:18px;right:14px;top:208px">
    <p style="margin-bottom:5px">This is a solid project located in the Bakken on top of the most cost-effective oil reserves anywhere in the Bakken, centrally located for business and with highway frontage and now with the new Bypass intersection at our doorstep, it creates an incredible opportunity.</p>
    <p>I would love to have you come on board as partner, our focus is pushing hard and fast to take advantage of the window of opportunity with the weather in March next year and have everything ready to roll and lots ready for sale before August 2019.</p>
  </div>
  <div class="ph" role="img" aria-label="Photograph of a hand placing a dart on a target beside a laptop and charts" style="left:0;top:262px;width:253px;height:100px;background:linear-gradient(160deg,#e9eef4 0%,#c8d3de 45%,#8f98a2 70%,#d6c27a 100%);clip-path:polygon(0 15%,100% 0,100% 100%,0 100%)"></div>
</section>

<!-- Row 3 : city development map -->
<section class="page tall" style="left:619px;top:798px">
  <div class="ph" role="img" aria-label="City development infographic: street map with new bypass, marked project sites, legend and aerial photos headed 'Watford City is re-investing in itself'" style="left:22px;top:22px;width:212px;height:318px;background:linear-gradient(180deg,#f4f6fa 0%,#e3e8f1 45%,#c9d0d8 75%,#eef0f3 100%)"></div>
</section>

<!-- Row 3 : back cover -->
<section class="page tall" style="left:910px;top:798px">
  <div class="ph" role="img" aria-label="Dusk photograph of a brick main street building with road light trails" style="inset:0;background:linear-gradient(180deg,#1f3f72 0%,#4f6c92 28%,#8a6a5a 55%,#6b5a58 75%,#b8b4b0 100%)"></div>
  <svg class="ph" style="inset:0" viewBox="0 0 253 362" width="253" height="362" aria-hidden="true">
    <polygon points="0,362 253,0 253,362" fill="#ffffff" opacity=".28"/>
  </svg>
  <div class="contact-box">
    <h3>Please send all questions and all<br>joint venture proposals to:</h3>
    <div class="contact-line"><svg viewBox="0 0 10 10"><circle cx="5" cy="5" r="5" fill="#fff"/><circle cx="5" cy="4" r="1.7" fill="#6b6f78"/><path d="M2.2 8.2a3 3 0 0 1 5.6 0" fill="#6b6f78"/></svg>Daniel Harlow</div>
    <div class="contact-line"><svg viewBox="0 0 10 10"><rect x=".5" y="2" width="9" height="6.5" rx=".8" fill="#fff"/><path d="M.8 2.4 5 5.8 9.2 2.4" stroke="#6b6f78" stroke-width=".8" fill="none"/></svg>dharlow.invest@mailbox.net</div>
    <div class="contact-line"><svg viewBox="0 0 10 10"><circle cx="5" cy="5" r="5" fill="#fff"/><path d="M3.3 2.5l1 1.4-.6.7a4 4 0 0 0 1.8 1.8l.7-.6 1.4 1-.6 1C5 7.7 2.4 5 2.3 3.1z" fill="#6b6f78"/></svg>+61 400 555 012</div>
  </div>
</section>

</body>
</html>
```